I need a website built for my modeling agency company.

On our website, a user can create a profile and we will submit it to thousands of modeling agents throughout the country.

In many cases, they will receive multiple offers from modeling agencies which allows them to pick and choose the contract that is best for them to launch their modeling career.

Some tag lines to consider using:

"Submit your profile to hundreds of modeling agents instantly!"

"Get found and become a star!"

We are: The Runway Guild.

Our Slogan: The World''s Largest Network of Fashion Models and Agents

What We Do: We are an agency with one of the largest networks of fashion professionals that are looking for new modeling talent. We host professional profiles for aspiring models, professional fashion models seeking work, modeling talent seekers, and top modeling agencies. We connect aspiring models with the top modeling agencies in the United States and abroad.

By submitting your FREE profile, you will be instantly introduced to the industry’s leading modeling agents. Within a few days, you could receive multiple, competing offers from modeling agencies that all want to launch your modeling career. Receiving multiple signing offers puts you in control of deciding which contract best suites you!

Reason: I've seen some good designs, but none that are 100% perfect. These are the ones that I like best so far (to give you some ideas): http://files.pixelvane.example/img/510372/820114/820114_4917263_510372_image.jpg http://files.pixelvane.example/img/510372/829305/829305_4926851_510372_image.jpg http://files.pixelvane.example/img/510372/51847/51847_4924097_510372_image.jpg http://files.pixelvane.example/img/510372/51847/51847_4919856_510372_image.jpg http://files.pixelvane.example/img/510372/823670/823670_4920438_510372_image.jpg

Target Market(s)

Aspiring models (mostly female, but some male)

Industry/Entity Type

Modeling Agency

Colors

Designer to choose colors to be used in the design.

Requirements
Nice to have
• Somewhere in the top half of the page, I would like there to be a small form for the visitor to fill out. This form will look as follows:

Title: Instantly contact hundreds of modeling agents who are looking for new talent and could make you a star!
Fields: First Name*, Last Name*, Age, Zip Code, Email Address*, Daytime Phone, Evening Phone, Comments.

Then, there will be a "submit" button to proceed to next step of form. Just below the "submit" button, should be the following verbiage: "You will have the opportunity to upload photo(s) and provide other pertinent information in next step."

```html
<!DOCTYPE html>
<html lang="en">
<head>
<meta charset="utf-8">
<title>The Runway Guild</title>
<link rel="stylesheet" href="https://fonts.googleapis.com/css2?family=Arimo:wght@400;700&family=Great+Vibes&display=swap">
<style>
:root{
  --page:#4f0a4f;
  --black:#000;
  --red:#e0202f;
  --red-deep:#c8101f;
  --wine:#3a0509;
  --white:#fff;
  --frame:#bdbdbd;
  --field-text:#222;
  --gray-panel:#2a2a2a;
  --sans:"Arimo",Arial,sans-serif;
  --script:"Great Vibes",cursive;
}
*{box-sizing:border-box;margin:0;padding:0}
html,body{width:897px;height:1200px;overflow:hidden}
body{position:relative;background:var(--page);font-family:var(--sans);color:var(--white)}
.abs{position:absolute}
.site-header{left:0;top:0;width:897px;height:97px;background:var(--black)}
.brand{left:28px;top:24px;display:flex;align-items:center;gap:10px}
.brand-mark{width:34px;height:34px;border-radius:50%;background:var(--red)}
.brand-name{font-size:27px;font-weight:400;color:var(--white);letter-spacing:1px}
.slogan{left:28px;top:70px;font-size:10px}
.social{display:flex;gap:4px}
.social span{width:20px;height:20px;border-radius:50%;display:block}
.s1{background:#2d5fa8}.s2{background:#2aa3dc}.s3{background:#2f8f3a}.s4{background:#c8202b}.s5{background:#f2a71b}
.header-social{left:754px;top:31px}
.search{left:582px;top:68px;display:flex}
.search-field{width:213px;height:22px;background:var(--white)}
.search-btn{width:82px;height:22px;background:var(--red);color:var(--white);font-size:15px;border:0;font-family:var(--sans)}
.main-nav{left:18px;top:99px;width:860px;height:30px;background:linear-gradient(#f0303d,#b80c18);display:flex;justify-content:center;align-items:center;font-size:13px}
.nav-list{display:flex;list-style:none}
.nav-list li+li::before{content:"|";margin:0 8px}
.hero{left:18px;top:136px;width:860px;height:278px;border:2px solid var(--frame);background:linear-gradient(#4a4a4a,#1a1a1a)}
.hero-photo{left:1px;top:1px;width:545px;height:273px;background:linear-gradient(90deg,#8b7a68,#4a3a30 40%,#6c6a55 60%,#2a2220)}
.hero-band{left:1px;top:193px;width:545px;height:81px;background:rgba(40,40,40,.75)}
.hero-script{left:110px;top:196px;font-family:var(--script);font-size:38px;color:var(--red)}
.hero-line{left:178px;top:222px;font-size:35px;color:var(--red)}
.profile-title{left:597px;top:12px;font-size:26px;color:var(--red)}
.script{font-family:var(--script)}
.profile-photo{left:565px;top:60px;width:274px;height:204px;background:linear-gradient(135deg,#7a7570,#2a2624)}
.content{left:18px;top:424px;width:860px;height:547px;border:1px solid var(--frame);background:linear-gradient(#0c0000,#5a0810 45%,var(--red) 100%)}
.h-red{color:var(--red);font-size:24px}
.what-title{left:24px;top:14px}
.what-text{left:24px;top:55px;width:515px;font-size:19.5px;line-height:23.5px;text-align:justify}
.aspiring-title{left:28px;top:193px}
.aspiring-text{left:31px;top:240px;width:240px;font-size:17px;line-height:21px}
.model-photo{top:305px;width:114px;height:172px}
.mp1{left:19px;background:linear-gradient(#7a4a3a,#3a2a22)}
.mp2{left:158px;background:linear-gradient(#e8d0d0,#c8a0b0)}
.name-tag{top:495px;width:102px;height:18px;background:linear-gradient(#b79ac7,#e7d5f0 50%,#8a6aa0);font-size:11px;font-weight:700;text-align:center;line-height:18px}
.nt1{left:26px}.nt2{left:165px}
.signup{left:292px;top:181px;width:254px;height:327px;border:1px solid var(--white);background:linear-gradient(#0a0000,#4a0508 60%,#b01020)}
.signup-title{left:10px;top:7px;width:236px;font-size:14px;line-height:16px}
.field{left:11px;width:225px;height:22px;background:var(--white);color:var(--field-text);font-size:11px;padding:5px 10px}
.field-half{width:104px}
.submit{left:172px;top:302px;width:63px;height:21px;background:linear-gradient(#f04050,#b80c18);border:1px solid #ddd;font-size:9px;color:var(--white);text-align:center;line-height:19px}
.signup-note{left:285px;top:514px;width:270px;text-align:center;font-size:11px;line-height:12px}
.fashion-title{left:580px;top:8px;font-size:46px;color:var(--red);line-height:1}
.models-title{left:679px;top:46px;font-size:30px;color:var(--red);letter-spacing:1px}
.feature{left:564px;width:286px;display:flex;gap:11px}
.feature-photo{width:78px;height:70px;flex:none;background:linear-gradient(#c9a28a,#5a3a30)}
.feature-photo.light{background:linear-gradient(#f0e0b0,#c8a088)}
.feature p{font-size:11px;line-height:11.7px;text-align:justify}
.post-more{left:771px;top:502px;font-size:13px}
.panel{top:975px;height:166px;border:1px solid var(--frame);background:linear-gradient(#000,#6a0812 45%,var(--red))}
.agencies{left:18px;width:420px}
.events{left:458px;width:420px}
.panel-title{left:14px;top:5px;font-size:25px}
.panel-title .script{font-size:36px}
.panel-title .cap{font-size:32px}
.panel-title .small{font-size:19px}
.agency-slot{top:50px;width:84px;height:88px;background:var(--white);border-radius:28px}
.event-text{top:53px;width:196px;font-size:11px;line-height:11.7px;text-align:justify}
.site-footer{left:0;top:1143px;width:897px;height:57px;background:var(--black)}
.footer-nav{left:0;top:8px;width:897px;display:flex;justify-content:center;font-size:11px}
.footer-social{left:408px;top:28px}
</style>
</head>
<body>
<header class="site-header abs">
  <div class="brand abs"><span class="brand-mark"></span><span class="brand-name">The Runway Guild</span></div>
  <div class="slogan abs">The World's Largest Network of Fashion Models and Agents</div>
  <div class="social header-social abs"><span class="s1"></span><span class="s2"></span><span class="s3"></span><span class="s4"></span><span class="s5"></span></div>
  <div class="search abs"><div class="search-field"></div><button class="search-btn">Search</button></div>
</header>

<nav class="main-nav abs">
  <ul class="nav-list"><li>HOME</li><li>ABOUT US</li><li>ASPIRING MODELS</li><li>PROFESSIONAL MODELS</li><li>AGENCIES</li><li>AGENTS</li><li>CONTACT US</li></ul>
</nav>

<section class="hero abs">
  <div class="hero-photo abs" role="img" aria-label="Four fashion models walking the runway"></div>
  <div class="hero-band abs"></div>
  <div class="hero-script abs">Get found and</div>
  <div class="hero-line abs">become a star!</div>
  <div class="profile-title abs"><span class="script">Create your</span> Profile</div>
  <div class="profile-photo abs" role="img" aria-label="Portrait of a model wearing a hat"></div>
</section>

<section class="content abs">
  <h2 class="what-title h-red abs"><span class="script">What</span> We Do....</h2>
  <p class="what-text abs">We are an association that hosts profiles for aspiring models, professional fashion models seeking work, modeling agencies, and modeling talent agents. We connect aspiring models with the top modeling agencies in the United States and abroad.</p>

  <h2 class="aspiring-title h-red abs"><span class="script" style="font-size:32px">Aspiring</span> Models....</h2>
  <p class="aspiring-text abs">Submit your profile to hundreds of modeling agents instantly!"</p>
  <div class="model-photo mp1 abs" role="img" aria-label="Aspiring model seated in a plaid outfit"></div>
  <div class="model-photo mp2 abs" role="img" aria-label="Aspiring model in a pink dress"></div>
  <div class="name-tag nt1 abs">NAME</div>
  <div class="name-tag nt2 abs">NAME</div>

  <form class="signup abs">
    <p class="signup-title abs">Instantly contact hundreds of modeling agents who are looking for new talent and could make you a star!</p>
    <div class="field abs" style="top:64px">First Name</div>
    <div class="field abs" style="top:92px">Last Name</div>
    <div class="field field-half abs" style="top:120px">Age</div>
    <div class="field field-half abs" style="top:120px;left:123px">Zip Code</div>
    <div class="field abs" style="top:149px">Email Address</div>
    <div class="field abs" style="top:177px">Daytime Phone</div>
    <div class="field abs" style="top:205px">Evening Phone</div>
    <div class="field abs" style="top:233px;height:66px">Comment</div>
    <div class="submit abs">SUBMIT</div>
  </form>
  <p class="signup-note abs">You will have the opportunity to upload photo(s) and provide other pertinent information in next step</p>

  <div class="fashion-title script abs">Fashion</div>
  <div class="models-title abs">MODELS</div>
  <div class="feature abs" style="top:86px"><div class="feature-photo" role="img" aria-label="Headshot of a fashion model"></div><p>Lorem ipsum dolor sit amet, consectetur adipisicing elit, sed do eiusmod tempor incididunt ut labore et dolore magna aliqua. Ut enim ad minim veniam, quis nostrud exercitation ullamco laboris nisi ut aliquip ex ea commodo consequat.</p></div>
  <div class="feature abs" style="top:189px"><div class="feature-photo light" role="img" aria-label="Headshot of a fashion model"></div><p>Lorem ipsum dolor sit amet, consectetur adipisicing elit, sed do eiusmod tempor incididunt ut labore et dolore magna aliqua. Ut enim ad minim veniam, quis nostrud exercitation ullamco laboris nisi ut aliquip ex ea commodo consequat.</p></div>
  <div class="feature abs" style="top:292px"><div class="feature-photo light" role="img" aria-label="Headshot of a fashion model"></div><p>Lorem ipsum dolor sit amet, consectetur adipisicing elit, sed do eiusmod tempor incididunt ut labore et dolore magna aliqua. Ut enim ad minim veniam, quis nostrud exercitation ullamco laboris nisi ut aliquip ex ea commodo consequat.</p></div>
  <div class="feature abs" style="top:395px"><div class="feature-photo" role="img" aria-label="Headshot of a fashion model"></div><p>Lorem ipsum dolor sit amet, consectetur adipisicing elit, sed do eiusmod tempor incididunt ut labore et dolore magna aliqua. Ut enim ad minim veniam, quis nostrud exercitation ullamco laboris nisi ut aliquip ex ea commodo consequat.</p></div>
  <div class="post-more abs">POST MORE</div>
</section>

<section class="panel agencies abs">
  <h2 class="panel-title abs"><span class="script">Modeling</span> <span class="cap">A</span><span class="small">GENCIES</span></h2>
  <div class="agency-slot abs" style="left:10px"></div>
  <div class="agency-slot abs" style="left:116px"></div>
  <div class="agency-slot abs" style="left:221px"></div>
  <div class="agency-slot abs" style="left:325px"></div>
</section>

<section class="panel events abs">
  <h2 class="panel-title abs"><span class="script">Upcoming</span> <span class="cap">E</span><span class="small">VENTS</span></h2>
  <p class="event-text abs" style="left:9px">Lorem ipsum dolor sit amet, consectetur adipisicing elit, sed do eiusmod tempor incididunt ut labore et dolore magna aliqua. Ut enim ad minim veniam, quis nostrud exercitation ullamco laboris nisi ut aliquip ex ea commodo consequat.</p>
  <p class="event-text abs" style="left:214px">Lorem ipsum dolor sit amet, consectetur adipisicing elit, sed do eiusmod tempor incididunt ut labore et dolore magna aliqua. Ut enim ad minim veniam, quis nostrud exercitation ullamco laboris nisi ut aliquip ex ea commodo consequat.</p>
</section>

<footer class="site-footer abs">
  <ul class="nav-list footer-nav abs"><li>HOME</li><li>ABOUT US</li><li>ASPIRING MODELS</li><li>PROFESSIONAL MODELS</li><li>AGENCIES</li><li>AGENTS</li><li>CONTACT US</li></ul>
  <div class="social footer-social abs"><span class="s1"></span><span class="s2"></span><span class="s3"></span><span class="s4"></span><span class="s5"></span></div>
</footer>
</body>
</html>
```